Internet plattform about horses with place for banners

We would like to redesign our website www.hufwelt-example.ch. We would like a simple, but modern & elegant design.
Of course the final design will be responive - but we'll start with the desktop design..

-> IMPORTANT: We will need place for 2 BANNERS: one 944x250 pixels and another 300x250px
-> We don't want any big image on the top - this takes too much place. (When we have no banners hired, we can put images of horses in place of the banners)
-> Background should be clear or white
-> Text on buttons should be text and no images
-> I would appreciate a smooth line somewhere that makes the whole design not too "rectangular"

A design we like is: www.sattelzone-example.ch (but don't do exactly the same)
-> see possible disposal of elements for top of the page -> new design.gif

On the startpage the most important are the news, as well as a new classifieds, new events .. exact content is not that important for this contest as we will offer our users possibility of choosing which content they will like.

I just upload some images you could use, but it's not a must.
If you need images, you could also take some ones on http://pferdfotos.lumbra-example.info/joomla/index.php (it's a friend of mine, so I would pay her the rights if we keep your project)

For this contest I don't expect different designs for mobile phones and don't need a css or anything else, just good ideas. Once we choose a partner this would be another job for you.

(Later, we'll work on the logo ...)

Target Market(s)

Swiss people who like horses and equestrian sports

Industry/Entity Type

Internet

Number of Pages Required

1 page

Font styles to use
Serif

Requirements
Must have
• Place for Maxiboard(944x250px) and halfpage(300x250) banners.
• The look should be modern, elegant and serious but not elitist. We should place banners for banks and other luxury sector, but all horse lovers should feel welcome. It should stay a popular site.
Nice to have
• A light element, a smooth or round line that makes the design not just rectangular...
• The design should leave much place for the information
• We leave the choice of colors open, but I like blue.. but will not be the only person to chose.
• You have the adress of our actual site (so feel free to open it - go on the contact page and send us a message,
Should not have
• no flashing design, no dark background, no big header.

```html
<!DOCTYPE html>
<html lang="en">
<head>
<meta charset="utf-8">
<title>Hufwelt – Horse Platform</title>
<link href="https://fonts.googleapis.com/css2?family=Arimo:wght@400;700&family=Cinzel:wght@400;700&display=swap" rel="stylesheet">
<style>
:root{
  --blue:#1b2d8f;
  --blue-dark:#14226e;
  --page-bg:#f3f1eb;
  --white:#ffffff;
  --text:#444444;
  --muted:#8a8a8a;
  --line:#dddddd;
  --banner-grey:#c9c9c9;
  --side-bg:#f5f5f5;
}
*{box-sizing:border-box;margin:0;padding:0}
html,body{width:1200px;height:1191px;overflow:hidden}
body{background:var(--page-bg);font-family:"Arimo",Arial,sans-serif;color:var(--text);position:relative}
.page{position:absolute;left:78px;top:0;width:1043px;height:1191px;background:var(--white);box-shadow:0 0 4px rgba(0,0,0,.12)}
.abs{position:absolute}
/* header */
.brand{left:11px;top:36px;display:flex;align-items:center;gap:8px;color:var(--blue-dark);font-family:"Cinzel",serif;font-size:30px;font-weight:700}
.brand-dot{width:22px;height:22px;border-radius:50%;background:var(--blue-dark)}
.search-box{left:769px;top:63px;width:174px;height:40px;border:1px solid var(--line);font-size:10px;color:#666;padding:15px 0 0 8px}
.search-box svg{position:absolute;right:10px;top:11px}
.lang-label{left:970px;top:56px;font-size:12px;color:var(--blue)}
.flag{width:23px;height:23px;border-radius:50%;overflow:hidden;top:81px}
.main-line{left:4px;top:129px;width:1035px;height:2px;background:var(--blue)}
.nav-notch{left:25px;top:130px;width:0;height:0;border-left:5px solid transparent;border-right:5px solid transparent;border-top:5px solid var(--blue)}
.main-nav{left:15px;top:143px;font-size:12px;color:#555;white-space:nowrap;word-spacing:1px}
.main-nav span.sep{margin:0 12px}
/* hero */
.hero{left:4px;top:172px;width:780px;height:207px;background:linear-gradient(100deg,#c9ccd0 0%,#a49f99 30%,#6b4a32 55%,#5a3a24 80%,#3d2d22 100%)}
.hero-bar{left:4px;top:312px;width:780px;height:67px;background:rgba(25,25,25,.75)}
.hero-label{left:4px;top:312px;width:90px;height:67px;background:var(--blue);color:#fff;font-weight:700;font-size:16px;line-height:20px;text-align:center;padding-top:14px}
.field{height:34px;width:266px;top:331px;border:1px solid #ddd;color:#ddd;font-size:12px;padding:9px 12px;white-space:nowrap}
.field svg{position:absolute;right:12px;top:14px}
.hero-btn{left:681px;top:331px;width:86px;height:33px;background:var(--blue);color:#fff;font-weight:700;font-size:12px;text-align:center;line-height:33px}
.side-banner{left:791px;top:172px;width:248px;height:207px;background:var(--banner-grey);text-align:center;color:#6d6d6d}
.side-banner .big{font-size:33px;margin-top:63px}
.side-banner .small{font-size:15px;margin-top:6px}
.sidebar-bg{left:791px;top:379px;width:248px;height:685px;background:var(--side-bg)}
/* headings */
.heading{font-family:"Cinzel",serif;font-weight:400;font-size:18px;color:#333;border-left:3px solid var(--blue);padding-left:6px;line-height:22px;letter-spacing:.5px;white-space:nowrap}
.intro{left:20px;top:461px;width:740px;font-size:10.7px;line-height:18px;color:#555}
/* circles */
.circle{width:212px;height:212px;border-radius:50%;top:586px;overflow:hidden}
.circle-1{left:17px;background:radial-gradient(circle at 55% 35%,#4a3a30,#5b4639 40%,#6d7077 90%)}
.circle-2{left:270px;background:linear-gradient(120deg,#2c2c2e 0%,#3a3a3c 45%,#9dbb6a 75%,#b7c98a 100%)}
.circle-3{left:524px;background:linear-gradient(180deg,#4b5a3a 0%,#6a8a45 45%,#8aa05c 70%,#dcdcd8 100%)}
.circle-caption{position:absolute;inset:0;background:rgba(60,60,70,.45);color:#fff;text-align:center;padding:83px 14px 0}
.circle-caption h3{font-size:14px;font-weight:700;letter-spacing:.5px}
.circle-caption i{display:block;width:56px;height:2px;background:var(--blue);margin:5px auto 9px}
.circle-caption p{font-size:10.5px;line-height:18px}
.divider{left:8px;top:843px;width:776px;height:1px;background:var(--line)}
.partner{background:#e4e4e4}
/* news */
.news{left:799px;width:234px;height:158px;background:#fff;border:1px solid #e3e3e3}
.date{position:absolute;left:2px;top:26px;width:31px;height:35px;background:var(--blue);color:#fff;font-size:10px;text-align:center;line-height:14px;padding-top:3px}
.date b{display:block;font-size:11px}
.news h4{position:absolute;left:50px;top:28px;width:180px;font-size:11.5px;line-height:18px;color:#333;letter-spacing:.3px}
.news p{position:absolute;left:50px;top:68px;width:180px;font-size:10.5px;line-height:16.5px;color:var(--muted)}
.read-more{position:absolute;right:10px;bottom:-1px;width:75px;height:18px;background:var(--blue);color:#fff;font-size:10.5px;text-align:center;line-height:18px}
/* contact */
.input{left:802px;width:229px;height:33px;background:#fff;border:1px solid #e6e6e6;font-size:10.5px;color:var(--muted);padding:11px 8px}
.submit{left:803px;top:977px;width:86px;height:33px;background:var(--blue);color:#fff;font-size:13px;text-align:center;line-height:33px}
/* footer */
.footer-bar{left:4px;top:1064px;width:1035px;height:6px;background:var(--blue)}
.footer-nav{left:0;top:1092px;width:1043px;text-align:center;font-size:11px;color:#888}
.footer-nav span.sep{margin:0 5px}
.social{top:1123px;width:26px;height:25px;background:#b9bdc8}
.copyright{left:0;top:1163px;width:1043px;text-align:center;font-size:11px;color:#888}
</style>
</head>
<body>
<div class="page">
  <div class="abs brand"><span class="brand-dot"></span>Hufwelt</div>

  <div class="abs search-box">Search..
    <svg width="18" height="18" viewBox="0 0 18 18"><circle cx="7" cy="7" r="5.5" fill="none" stroke="#777" stroke-width="2"/><line x1="11" y1="11" x2="16" y2="16" stroke="#777" stroke-width="2.5" stroke-linecap="round"/></svg>
  </div>
  <div class="abs lang-label">Language:</div>
  <svg class="abs flag" style="left:970px" viewBox="0 0 23 23" role="img" aria-label="German"><rect width="23" height="8" fill="#222"/><rect y="8" width="23" height="7" fill="#d00"/><rect y="15" width="23" height="8" fill="#fc0"/></svg>
  <svg class="abs flag" style="left:1000px" viewBox="0 0 23 23" role="img" aria-label="French"><rect width="8" height="23" fill="#1d4fb8"/><rect x="8" width="7" height="23" fill="#fff"/><rect x="15" width="8" height="23" fill="#e1252f"/></svg>

  <div class="abs main-line"></div>
  <div class="abs nav-notch"></div>
  <nav class="abs main-nav">Home<span class="sep">|</span>Classified<span class="sep">|</span>horses<span class="sep">|</span>Directory<span class="sep">|</span>calendar<span class="sep">|</span>Horse pictures<span class="sep">|</span>forum<span class="sep">|</span>Links<span class="sep">|</span>Our partners<span class="sep">|</span>contact<span class="sep">|</span>About Hufwelt<span class="sep">|</span>Login My Hufwelt</nav>

  <div class="abs hero" role="img" aria-label="Young man resting his head against a brown horse"></div>
  <div class="abs hero-bar"></div>
  <div class="abs hero-label">Search<br>horse</div>
  <div class="abs field" style="left:118px">Category
    <svg width="12" height="7" viewBox="0 0 12 7"><path d="M1 1l5 4 5-4" fill="none" stroke="#fff" stroke-width="2"/></svg></div>
  <div class="abs field" style="left:397px">Keywords
    <svg width="12" height="7" viewBox="0 0 12 7"><path d="M1 1l5 4 5-4" fill="none" stroke="#fff" stroke-width="2"/></svg></div>
  <div class="abs hero-btn">Search</div>

  <div class="abs side-banner"><div class="big">banner</div><div class="small">300 X 250</div></div>
  <div class="abs sidebar-bg"></div>

  <h2 class="abs heading" style="left:19px;top:418px">Wel come to hufwelt-example.ch</h2>
  <p class="abs intro">Lorem ipsum dolor sit amet, consectetur adipiscing elit, sed do eiusmod tempor incididunt ut &nbsp;nisi ut aliquip ex ea commodo consequat. Duis aute irure dolor in reprehenderit in voluptate velit esse cillum dolore eu fugiat nulla pariatur. Sed ut perspiciatis unde omnis iste natus error sit voluptatem accusantium doloremque laudantium. Excepteur sint occaecat cupidatat non proident, sunt in culpa qui officia deserunt mollit anim id est laborum emque laudantium.</p>

  <div class="abs circle circle-1" role="img" aria-label="Galloping brown horse with flowing mane">
    <div class="circle-caption"><h3>Lorem ipsum dolor</h3><i></i><p>Lorem ipsum dolor sit amet, consec-tetur adipiscing elit, sed do eiusmod tempor incididunt</p></div>
  </div>
  <div class="abs circle circle-2" role="img" aria-label="Woman close to a dark horse's head on a meadow"></div>
  <div class="abs circle circle-3" role="img" aria-label="Bride in white dress with a horse on a paddock"></div>

  <div class="abs divider"></div>
  <div class="abs partner" style="left:35px;top:894px;width:68px;height:67px"></div>
  <div class="abs partner" style="left:159px;top:898px;width:162px;height:49px"></div>
  <div class="abs partner" style="left:380px;top:908px;width:150px;height:31px"></div>
  <div class="abs partner" style="left:588px;top:904px;width:158px;height:40px"></div>

  <h2 class="abs heading" style="left:803px;top:412px">Latest News</h2>
  <article class="abs news" style="top:450px">
    <div class="date"><b>09</b>Nov</div>
    <h4>Lorem ipsum dolor sit amet, consectetur eiusmod.</h4>
    <p>Sed ut perspiciatis unde omnis iste natus error sit voluptatem accusan-tium doloremque.</p>
    <div class="read-more">Read More</div>
  </article>
  <article class="abs news" style="top:608px">
    <div class="date"><b>09</b>Nov</div>
    <h4>Lorem ipsum dolor sit amet, consectetur eiusmod.</h4>
    <p>Sed ut perspiciatis unde omnis iste natus error sit voluptatem accusan-tium doloremque.</p>
    <div class="read-more">Read More</div>
  </article>

  <h2 class="abs heading" style="left:803px;top:791px">Contact Us</h2>
  <div class="abs input" style="top:821px">Your Name</div>
  <div class="abs input" style="top:863px">Email</div>
  <div class="abs input" style="top:905px;height:57px">Message</div>
  <div class="abs submit">Submit</div>

  <div class="abs footer-bar"></div>
  <nav class="abs footer-nav">Home<span class="sep">|</span>Classified<span class="sep">|</span>horses<span class="sep">|</span>Directory<span class="sep">|</span>calendar<span class="sep">|</span>Horse pictures<span class="sep">|</span>forum<span class="sep">|</span>Links<span class="sep">|</span>Our partners<span class="sep">|</span>contact<span class="sep">|</span>About Hufwelt<span class="sep">|</span>Login My Hufwelt</nav>
  <div class="abs social" style="left:471px"></div>
  <div class="abs social" style="left:506px"></div>
  <div class="abs social" style="left:540px"></div>
  <div class="abs social" style="left:575px"></div>
  <div class="abs copyright">Copyright 2014 hufwelt-example.ch | All right reserved</div>
</div>
</body>
</html>
```